TaskNib iOS App Icon Design

TaskNib is an iOS app currently in development (see here for an early screenshot of the UI: https://social.example/Plovencraft/status/918273645501928374/photo/1). This app makes it easier to take notes during meetings.

I am looking for an icon that will capture the essence of both note-taking & calendars. Perhaps a pencil icon over a calendar grid? I'm open to creativity. Please optimize the icon for iOS 7. It would be great if the colors could involve the same red (#ff0000) that's used in the screenshot link above.

The icon must be at least 1024x1024. Both psd and vector deliverables are required.

Target Market(s)

Targeting professionals who work in an office and attend meetings on a regular basis.

Requirements
Must have
• Follow Quillon's icon guidelines for iOS 7: https://devs.quillon.example/library/ios/documentation/userexperience/conceptual/MobileHIG/AppIcons.html#//apple_ref/doc/uid/TP40006556-CH19-SW1
- Icon must be at least 1024x1024.
- Final deliverables must be in psd and vector formats.
Nice to have
• Would be great if red (#ff0000) could be involved in the color theme.
Should not have
• Rounded corners
- Drop shadow

```html
<!DOCTYPE html>
<html lang="en">
<head>
<meta charset="utf-8">
<title>TaskNib – To Do</title>
<link rel="stylesheet" href="https://fonts.googleapis.com/css2?family=Fredoka+One&display=swap">
<style>
  :root {
    --brand-red: #ff0000;
    --shadow-red: #ee3b3b;
    --paper: #ffffff;
    --canvas: #ffffff;
  }
  * { margin: 0; padding: 0; box-sizing: border-box; }
  html, body {
    width: 1200px;
    height: 1200px;
    overflow: hidden;
    background: var(--canvas);
  }
  .icon {
    position: relative;
    width: 1200px;
    height: 1200px;
  }
  .note-card {
    position: absolute;
    left: 0;
    top: 0;
    width: 1172px;
    height: 1148px;
    background: var(--paper);
    border-radius: 0 0 6px 0;
    box-shadow: 16px 16px 0 var(--shadow-red);
  }
  .title-band {
    position: absolute;
    left: 5px;
    top: 6px;
    width: 1167px;
    height: 194px;
    background: var(--brand-red);
    border-radius: 10px;
  }
  .note-text {
    position: absolute;
    left: 0;
    top: 0;
    width: 1200px;
    height: 1200px;
  }
  .note-text text {
    font-family: "Fredoka One", "Arial Rounded MT Bold", "Varela Round", sans-serif;
    text-transform: uppercase;
  }
  .app-name { fill: var(--paper); font-size: 190px; }
  .list-heading { fill: var(--brand-red); font-size: 300px; }
  .task { fill: var(--brand-red); font-size: 130px; }
  .bullet { fill: var(--brand-red); }
</style>
</head>
<body>
  <main class="icon">
    <section class="note-card">
      <div class="title-band"></div>
    </section>
    <svg class="note-text" viewBox="0 0 1200 1200" xmlns="http://www.w3.org/2000/svg">
      <title>TaskNib – To Do: Do Action, Move Item</title>
      <text class="app-name" x="588" y="168" text-anchor="middle" textLength="880" lengthAdjust="spacingAndGlyphs">TaskNib</text>
      <text class="list-heading" x="36" y="463" textLength="948" lengthAdjust="spacingAndGlyphs">To Do :</text>
      <circle class="bullet" cx="117" cy="672" r="37"/>
      <text class="task" x="246" y="709" textLength="642" lengthAdjust="spacingAndGlyphs">Do Action</text>
      <circle class="bullet" cx="124" cy="886" r="37"/>
      <text class="task" x="248" y="921" textLength="633" lengthAdjust="spacingAndGlyphs">Move Item</text>
    </svg>
  </main>
</body>
</html>
```